New Business Card (to reflect updated website content and graphics)

I changed some text and graphics on my website, so I need a new business card.

Target Market(s)

Mostly women, ages 30 - 60.

Industry/Entity Type

Life Coaching

Contact Information for Business Card

Included in attached Word document

Font styles to use
Sans Serif

Requirements
Must have
• I am not a creative person, so I will defer to designer. Take a look at my website, and you can get a feel for me, my style, and my target audience. Thank You!

My 3 branding colors are included in attached Word document.

```html
<!DOCTYPE html>
<html lang="en">
<head>
<meta charset="utf-8">
<title>Bloom Forward Coaching – Business Card</title>
<link href="https://fonts.googleapis.com/css2?family=Montserrat:wght@400;500;700&display=swap" rel="stylesheet">
<style>
  :root {
    --teal: #2e9bb5;
    --teal-wash: #d7ecf1;
    --coral-wash: #fbe3df;
    --ink: #1a1a1a;
    --ink-soft: #2a2a2a;
    --paper: #ffffff;
    --stage: #d9d9d9;
    --text-light: #f2f2f2;
  }
  * { box-sizing: border-box; margin: 0; padding: 0; }
  html, body { width: 1200px; height: 881px; overflow: hidden; }
  body {
    background: var(--stage);
    font-family: "Montserrat", Arial, sans-serif;
    display: flex; flex-direction: column; align-items: center; justify-content: center; gap: 40px;
  }
  .card {
    width: 700px; height: 400px; border-radius: 22px; position: relative; overflow: hidden;
    box-shadow: 0 8px 24px rgba(0,0,0,.18);
  }
  .card-front { background: var(--paper); display: flex; align-items: center; justify-content: center; }
  .word-cloud-area {
    width: 340px; height: 240px; border-radius: 12px;
    background: linear-gradient(135deg, var(--teal-wash), var(--coral-wash));
  }

  .card-back {
    background: linear-gradient(100deg, var(--ink-soft) 0%, var(--ink) 40%, #222 100%);
    color: var(--text-light);
    display: flex; flex-direction: column; align-items: center;
    padding-top: 42px;
  }
  .brand { color: var(--teal); text-align: center; font-weight: 500; }
  .brand-name { font-size: 34px; letter-spacing: 1px; }
  .brand-sub { font-size: 18px; letter-spacing: 14px; margin-top: 6px; padding-left: 14px; }
  .person-name {
    color: var(--teal); font-weight: 700; font-size: 36px; letter-spacing: 5px; margin-top: 34px;
  }
  .person-title { font-size: 15px; text-align: center; line-height: 1.45; margin-top: 8px; }
  .divider { display: flex; align-items: center; gap: 10px; width: 560px; margin-top: 18px; }
  .divider-line { flex: 1; height: 1px; background: var(--teal); }
  .icon { width: 26px; height: 26px; }
  .contact-line { font-size: 17px; margin-top: 14px; }
  .contact-line .sep { color: var(--teal); margin: 0 8px; }
  .contact-email { font-size: 17px; margin-top: 8px; }
</style>
</head>
<body>
  <section class="card card-front">
    <div class="word-cloud-area" role="img" aria-label="Word cloud illustration of coaching themes such as hope, joy, love, peace and clarity, with the slogan Feel Better, Live Well"></div>
  </section>

  <section class="card card-back">
    <div class="brand">
      <div class="brand-name">Bloom Forward</div>
      <div class="brand-sub">COACHING</div>
    </div>
    <div class="person-name">DANA WHITFIELD</div>
    <p class="person-title">Certified Professional Life Coach | Health &amp; Wellness Coach<br>Advanced Loss Renewal Method Specialist</p>
    <div class="divider">
      <span class="divider-line"></span>
      <svg class="icon" viewBox="0 0 26 26" aria-label="Phone"><circle cx="13" cy="13" r="12" fill="none" stroke="var(--teal)" stroke-width="1.5"/><path d="M9 7 l3 3 -1.5 1.5 c1 2 2 3 4 4 L16 14 l3 3 -2 2 C11 18 8 15 7 9 Z" fill="none" stroke="var(--teal)" stroke-width="1.3"/></svg>
      <svg class="icon" viewBox="0 0 26 26" aria-label="Email"><circle cx="13" cy="13" r="12" fill="none" stroke="var(--teal)" stroke-width="1.5"/><rect x="7" y="9" width="12" height="8" fill="none" stroke="var(--teal)" stroke-width="1.3"/><path d="M7 9 l6 5 6-5" fill="none" stroke="var(--teal)" stroke-width="1.3"/></svg>
      <svg class="icon" viewBox="0 0 26 26" aria-label="Website"><circle cx="13" cy="13" r="12" fill="none" stroke="var(--teal)" stroke-width="1.5"/><circle cx="13" cy="13" r="6.5" fill="none" stroke="var(--teal)" stroke-width="1.2"/><ellipse cx="13" cy="13" rx="3" ry="6.5" fill="none" stroke="var(--teal)" stroke-width="1.2"/><path d="M6.5 13 h13" stroke="var(--teal)" stroke-width="1.2"/></svg>
      <span class="divider-line"></span>
    </div>
    <p class="contact-line">(555) 014-2290<span class="sep">|</span>www.bloomforwardcoaching.com</p>
    <p class="contact-email">dana@bloomforwardcoaching.com</p>
  </section>
</body>
</html>
```